Business Consulting Business Card

professional business card with basic information (1) First and Last name (2) email address, (3) phone number, (4) website.

```html
<!DOCTYPE html>
<html lang="en">
<head>
<meta charset="UTF-8">
<title>Harbor Lane – Business Card</title>
<link href="https://fonts.googleapis.com/css2?family=Montserrat:wght@500;700&family=Open+Sans:wght@400&display=swap" rel="stylesheet">
<style>
  :root {
    --navy: #0b2a40;
    --teal: #4fc3c4;
    --teal-deep: #3fa9c9;
    --white: #ffffff;
    --ink: #2f3a44;
    --grey: #555d66;
    --backdrop: #e3e6ea;
  }
  * { margin: 0; padding: 0; box-sizing: border-box; }
  html, body { width: 1200px; height: 1000px; overflow: hidden; }
  body {
    background: var(--backdrop);
    display: flex;
    flex-direction: column;
    align-items: center;
    justify-content: center;
    gap: 44px;
    font-family: "Montserrat", sans-serif;
  }
  .card {
    position: relative;
    width: 760px;
    height: 434px;
    border-radius: 24px;
    overflow: hidden;
    box-shadow: 0 10px 30px rgba(0,0,0,0.18);
  }
  .card--front {
    background: var(--navy);
    display: flex;
    align-items: center;
    justify-content: center;
  }
  .brand {
    display: flex;
    align-items: center;
    gap: 26px;
  }
  .brand__dot {
    width: 74px;
    height: 74px;
    border-radius: 50%;
    background: var(--teal);
  }
  .brand__name {
    font-family: "Montserrat", sans-serif;
    font-weight: 500;
    font-size: 40px;
    letter-spacing: 0.42em;
    color: var(--white);
  }
  .card--back { background: var(--white); }
  .card__band {
    position: absolute;
    inset: 0;
    width: 100%;
    height: 100%;
  }
  .band-dark { fill: var(--navy); }
  .band-swoosh { fill: var(--teal); }
  .holder {
    position: absolute;
    left: 56px;
    top: 150px;
  }
  .holder__name {
    font-family: "Montserrat", sans-serif;
    font-weight: 700;
    font-size: 25px;
    letter-spacing: 0.1em;
    color: var(--teal);
  }
  .holder__title {
    font-family: "Open Sans", sans-serif;
    font-size: 17px;
    color: var(--grey);
    margin-top: 4px;
  }
  .contacts {
    position: absolute;
    left: 56px;
    bottom: 44px;
    list-style: none;
    font-family: "Open Sans", sans-serif;
    font-size: 17px;
    color: var(--ink);
    line-height: 1.7;
  }
  .contacts li { display: flex; align-items: center; gap: 10px; }
  .contacts svg { width: 13px; height: 13px; fill: var(--ink); flex: none; }
  .card--back .brand {
    position: absolute;
    right: 50px;
    top: 250px;
    gap: 20px;
  }
  .card--back .brand__dot { width: 54px; height: 54px; }
  .card--back .brand__name {
    font-size: 28px;
    color: var(--navy);
  }
</style>
</head>
<body>

<section class="card card--front" aria-label="Card front">
  <div class="brand">
    <span class="brand__dot"></span>
    <span class="brand__name">HARBOR LANE</span>
  </div>
</section>

<section class="card card--back" aria-label="Card back">
  <svg class="card__band" viewBox="0 0 760 434" preserveAspectRatio="none" aria-hidden="true">
    <path class="band-dark" d="M0 0 H760 V172 Q400 96 0 78 Z"/>
    <path class="band-swoosh" d="M130 88 Q470 118 760 172 V190 Q460 124 130 88 Z"/>
  </svg>

  <div class="holder">
    <h1 class="holder__name">MARTEN HALE</h1>
    <p class="holder__title">General Manager</p>
  </div>

  <ul class="contacts">
    <li>
      <svg viewBox="0 0 24 24"><path d="M6.6 10.8a15.1 15.1 0 006.6 6.6l2.2-2.2a1 1 0 011-.25 11.4 11.4 0 003.6.57 1 1 0 011 1V20a1 1 0 01-1 1A17 17 0 013 4a1 1 0 011-1h3.5a1 1 0 011 1c0 1.25.2 2.45.57 3.57a1 1 0 01-.25 1z"/></svg>
      555-014-2287
    </li>
    <li>
      <svg viewBox="0 0 24 24"><path d="M2 5h20v14H2z M2 5l10 8 10-8" fill="none" stroke="#2f3a44" stroke-width="2.4"/></svg>
      hello@harborlane.com
    </li>
    <li>
      <svg viewBox="0 0 24 24"><circle cx="12" cy="12" r="10" fill="none" stroke="#2f3a44" stroke-width="2.2"/><path d="M2 12h20M12 2c3 3 3 17 0 20M12 2c-3 3-3 17 0 20" fill="none" stroke="#2f3a44" stroke-width="1.8"/></svg>
      www.harborlane.com
    </li>
  </ul>

  <div class="brand">
    <span class="brand__dot"></span>
    <span class="brand__name">HARBOR LANE</span>
  </div>
</section>

</body>
</html>
```